Poster Needed for Church Conference

I need a poster for a weekend conference at my church. Looking to attract as many people as possible. We are a church in the suburbs of Houston. This is mainly for our own church members but we are opening it up to outside church members.

Please see previous design from last conference and all other graphic work that can (doesn't need to be) included.

Target Market(s)

It's targeted for all people. But our main audience is families. around the age of 30 should be main target.

Industry/Entity Type

Non-Profit

Font styles to use
Serif
Sans Serif

Colors

Designer to choose colors to be used in the design.

Requirements
Must have
• 11x17 design with ability to shrink and blow up. but ideally for 11x17
• Content and wording:
• "Rooted Lantern Conference: Bridging the gap between generations and passing on our deepest beliefs and values."
• Featuring Dr. Glen Marlowe. Author of "The Map of Q9"
• Aug 25-26: Friday 8-10 pm, Saturday 4-8 pm
• Cost Adults $15/Children $5: Covers admission to all sessions and workshops, refreshments and Saturday dinner. *kids 5 and under free
• Childcare provided for all sessions. "
• Please use church logo and address on flyer: 4312 Orchard Bend, Missouri City, TX 77512
Nice to have
• Ideally it will be designed so that we can crop a 16:9 pp announcement slide and header for our website.
Should not have
• anything offensive

```html
<!DOCTYPE html>
<html lang="en">
<head>
<meta charset="utf-8">
<title>Rooted Lantern Conference</title>
<link href="https://fonts.googleapis.com/css2?family=Montserrat:wght@400;500;700;800&family=Bebas+Neue&display=swap" rel="stylesheet">
<style>
  :root{
    --navy:#0f2a44;
    --cyan:#3cbfe6;
    --green:#39b54a;
    --lime:#b7d531;
    --blue:#2a7fd0;
    --deep:#2b3fa0;
    --paper:#ffffff;
    --backdrop:#e9ecef;
    --line:#d6dde3;
  }
  *{box-sizing:border-box;margin:0;padding:0}
  html,body{width:1200px;height:1200px;overflow:hidden;background:var(--backdrop)}
  body{position:relative;font-family:"Montserrat",sans-serif;color:var(--navy)}
  .poster{position:absolute;left:40px;top:235px;width:1120px;height:730px;background:var(--paper);overflow:hidden;box-shadow:0 6px 24px rgba(0,0,0,.12)}
  .poster > *{position:absolute}
  .grid-lines{left:0;top:0;width:1120px;height:730px}
  .crystals-top{left:0;top:0;width:430px;height:330px}
  .crystals-corner{right:0;bottom:0;width:180px;height:150px}
  .speaker-photo{left:200px;top:215px;width:235px;height:220px}
  .book{left:890px;top:215px;width:110px;height:170px;background:linear-gradient(160deg,#f4f6f7,#dfe4e6 70%,#cfd6d9);border:1px solid #cdd3d6;box-shadow:4px 4px 8px rgba(0,0,0,.15)}
  .book-band{position:absolute;left:0;right:0;top:105px;height:14px;background:var(--green)}
  .headline{left:440px;top:62px;font-weight:800;font-size:44px;letter-spacing:-1.4px;line-height:1;white-space:nowrap}
  .tagline{left:440px;top:118px;width:620px;font-weight:500;font-size:28px;line-height:1.18;color:var(--cyan);letter-spacing:-.8px}
  .speaker{left:465px;top:325px;width:400px}
  .speaker-name{font-weight:800;font-size:25px;color:var(--green);letter-spacing:-.6px;white-space:nowrap}
  .speaker-bio{font-size:14px;color:var(--green);line-height:1.3;margin-top:4px}
  .cost{left:465px;top:440px;width:580px}
  .cost-line{font-weight:700;font-size:25px;letter-spacing:-.6px;white-space:nowrap}
  .cost-line .price{font-family:"Bebas Neue",sans-serif;font-weight:400;font-size:42px;color:var(--cyan);letter-spacing:0}
  .cost-note{font-size:15px;line-height:1.3;letter-spacing:-.3px}
  .cost-note .free{color:var(--cyan)} .cost-note .free b{font-weight:800}
  .info{left:465px;top:562px;font-size:15px;line-height:1.35;letter-spacing:-.3px}
  .info .web{color:var(--blue);font-weight:700}
  .dates{left:90px;top:468px;width:250px;text-align:center;font-family:"Bebas Neue",sans-serif}
  .dates-month{font-size:70px;line-height:.9;color:var(--navy)}
  .dates-days{font-size:120px;line-height:.85;color:var(--cyan)}
  .dates-times{font-size:28px;line-height:1.1;color:var(--navy);margin-top:6px}
  .church{left:640px;top:632px;display:flex;flex-direction:column;align-items:flex-start}
  .church-name{display:flex;align-items:center;gap:10px;font-weight:500;font-size:22px;color:var(--green);letter-spacing:.5px;white-space:nowrap}
  .church-dot{width:18px;height:18px;border-radius:50%;background:var(--green)}
  .church-address{font-weight:700;font-size:13.5px;color:var(--blue);margin-top:6px;white-space:nowrap}
</style>
</head>
<body>
<main class="poster">
  <svg class="grid-lines" viewBox="0 0 1120 730" aria-hidden="true">
    <g fill="none" stroke="var(--line)" stroke-width="1">
      <path d="M560 40 L620 100 L680 40"/>
      <path d="M560 260 L620 200 L680 260 L620 320 Z"/>
      <path d="M900 30 L980 110 L1060 30"/>
      <path d="M1010 160 L1070 220 L1010 280"/>
      <path d="M40 460 L200 320"/>
    </g>
  </svg>

  <svg class="crystals-top" viewBox="0 0 430 330" role="img" aria-label="Faceted crystal shapes in blue, teal and lime">
    <defs>
      <linearGradient id="crystalA" x1="0" y1="0" x2="1" y2="1">
        <stop offset="0" stop-color="#7fd3f2"/><stop offset=".45" stop-color="#2a9fd8"/><stop offset=".75" stop-color="#25b49a"/><stop offset="1" stop-color="#b7d531"/>
      </linearGradient>
    </defs>
    <path d="M0 30 L140 10 L300 0 L410 15 L390 100 L320 160 L260 220 L200 250 L120 320 L60 290 L0 250 Z" fill="url(#crystalA)" opacity=".92"/>
  </svg>

  <svg class="crystals-corner" viewBox="0 0 180 150" role="img" aria-label="Faceted crystal shapes in blue and green">
    <defs>
      <linearGradient id="crystalB" x1="0" y1="1" x2="1" y2="0">
        <stop offset="0" stop-color="#39b54a"/><stop offset=".5" stop-color="#3cbfe6"/><stop offset="1" stop-color="#2a7fd0"/>
      </linearGradient>
    </defs>
    <path d="M40 150 L90 100 L140 60 L180 10 L180 150 Z" fill="url(#crystalB)"/>
  </svg>

  <svg class="speaker-photo" viewBox="0 0 235 220" role="img" aria-label="Portrait photo of Dr. Glen Marlowe">
    <defs>
      <linearGradient id="photoTone" x1="0" y1="0" x2="1" y2="1">
        <stop offset="0" stop-color="#6b6f73"/><stop offset=".5" stop-color="#c9a48a"/><stop offset="1" stop-color="#2b2b2b"/>
      </linearGradient>
    </defs>
    <path d="M215 0 L215 220 L235 220 L235 130 Z" fill="var(--deep)"/>
    <path d="M5 130 L215 0 L215 220 Z" fill="url(#photoTone)"/>
    <path d="M150 220 L235 175 L235 220 Z" fill="var(--lime)"/>
  </svg>

  <h1 class="headline">Rooted Lantern Conference:</h1>
  <p class="tagline">Bridging the gap between generations and passing on our deepest beliefs and values.</p>

  <section class="speaker">
    <h2 class="speaker-name">Featuring Dr. Glen Marlowe.</h2>
    <p class="speaker-bio">Author of The Map of Q9, Founder of Hearthline Ministries and Expert in Parent/Children relationships.</p>
  </section>

  <div class="book" role="img" aria-label="Cover of the book The Map of Q9"><div class="book-band"></div></div>

  <section class="cost">
    <p class="cost-line">Cost : Adults <span class="price">$15,</span> Children <span class="price">$5:</span></p>
    <p class="cost-note">Covers admission to all sessions and workshops, refreshments and Saturday dinner. <span class="free">*kids 5 and under <b>FREE</b></span></p>
  </section>

  <p class="info">Childcare provided for all sessions.<br>For more info visit <span class="web">www.cedarhollowchurch.org</span></p>

  <section class="dates">
    <p class="dates-month">August</p>
    <p class="dates-days">25-26</p>
    <p class="dates-times">Friday 8-10 PM<br>Saturday 4-8 PM</p>
  </section>

  <footer class="church">
    <p class="church-name"><span class="church-dot"></span>Cedar Hollow Community Church</p>
    <p class="church-address">4312 Orchard Bend, Missouri City, TX 77512</p>
  </footer>
</main>
</body>
</html>
```